Birchline Septic Solutions

Would like to see some single sided ones but would also like to see some double sided with one sided only being the logo. Owners name is Tom Halvick. Phone number is 555-214-0387
Services are pumping, inspections, installs, and repairs

Contact Information for Business Card

555-241-0387 Tom Halvick Cedarbrook, OH

```html
<!DOCTYPE html>
<html lang="en">
<head>
<meta charset="utf-8">
<title>Birchline Septic Solutions – Business Cards</title>
<link rel="stylesheet" href="https://fonts.googleapis.com/css2?family=Marcellus&display=swap">
<style>
  :root {
    --bg: #e4e5e8;
    --card: #ffffff;
    --ink: #0b0b0c;
    --teal: #2bb5b0;
    --mist: #ececec;
    --mist-dark: #d9d9d9;
    --white: #ffffff;
  }
  * { box-sizing: border-box; margin: 0; padding: 0; }
  html, body { width: 1200px; height: 800px; overflow: hidden; }
  body {
    background: var(--bg);
    display: flex;
    align-items: center;
    justify-content: center;
    gap: 40px;
    font-family: "Marcellus", serif;
  }
  .card {
    position: relative;
    width: 540px;
    height: 309px;
    background: var(--card);
    overflow: hidden;
    box-shadow: 0 6px 18px rgba(0,0,0,0.12);
  }
  .card__scenery {
    position: absolute;
    left: 0; right: 0; top: 30px; bottom: 0;
    background: linear-gradient(180deg, var(--white) 0%, var(--mist) 55%, var(--mist-dark) 100%);
    opacity: 0.75;
  }
  .card__brand {
    position: absolute;
    left: 0; right: 0; top: 46px;
    display: flex;
    align-items: center;
    justify-content: center;
    gap: 14px;
  }
  .card__brand-mark {
    width: 16px; height: 16px;
    background: var(--ink);
    border-radius: 50%;
  }
  .card__brand-name {
    font-family: "Marcellus", serif;
    font-size: 30px;
    letter-spacing: 3px;
    text-transform: uppercase;
    color: var(--ink);
    text-align: center;
    line-height: 1.15;
  }
  .card__band {
    position: absolute;
    left: 0; right: 0; bottom: 0;
    height: 112px;
    background: var(--ink);
    border-top: 4px solid var(--teal);
    display: flex;
    align-items: center;
    justify-content: center;
  }
  .services { text-align: center; }
  .services__title {
    color: var(--teal);
    font-size: 19px;
    letter-spacing: 0.5px;
    margin-bottom: 6px;
  }
  .services__list { color: var(--white); font-size: 17px; }
  .contact { display: flex; align-items: center; gap: 18px; }
  .contact__person { text-align: right; }
  .contact__name { color: var(--teal); font-size: 21px; }
  .contact__role { color: var(--white); font-size: 16px; margin-top: 4px; }
  .contact__divider { width: 1px; height: 52px; background: var(--teal); }
  .contact__lines { display: flex; flex-direction: column; gap: 8px; }
  .contact__line {
    display: flex; align-items: center; gap: 8px;
    color: var(--white); font-size: 17px;
  }
  .contact__icon { width: 15px; height: 15px; fill: var(--teal); flex: none; }
</style>
</head>
<body>

  <section class="card card--services">
    <div class="card__scenery" role="img" aria-label="Faint grey pine forest and mountain illustration"></div>
    <div class="card__brand">
      <span class="card__brand-mark"></span>
      <span class="card__brand-name">Birchline<br>Septic Solutions</span>
    </div>
    <div class="card__band">
      <div class="services">
        <p class="services__title">OUR SERVICES</p>
        <p class="services__list">Pumping, Inspections, Installs, And Repairs</p>
      </div>
    </div>
  </section>

  <section class="card card--contact">
    <div class="card__scenery" role="img" aria-label="Faint grey pine forest and mountain illustration"></div>
    <div class="card__brand">
      <span class="card__brand-mark"></span>
      <span class="card__brand-name">Birchline<br>Septic Solutions</span>
    </div>
    <div class="card__band">
      <div class="contact">
        <div class="contact__person">
          <p class="contact__name">TOM HALVICK</p>
          <p class="contact__role">Owners</p>
        </div>
        <span class="contact__divider"></span>
        <div class="contact__lines">
          <p class="contact__line">
            <svg class="contact__icon" viewBox="0 0 24 24" aria-hidden="true"><path d="M6.6 10.8a15.1 15.1 0 0 0 6.6 6.6l2.2-2.2a1 1 0 0 1 1-.25 11.4 11.4 0 0 0 3.6.57 1 1 0 0 1 1 1V20a1 1 0 0 1-1 1A17 17 0 0 1 3 4a1 1 0 0 1 1-1h3.5a1 1 0 0 1 1 1c0 1.25.2 2.45.57 3.57a1 1 0 0 1-.25 1z"/></svg>
            555-241-0387
          </p>
          <p class="contact__line">
            <svg class="contact__icon" viewBox="0 0 24 24" aria-hidden="true"><path d="M12 2a7 7 0 0 0-7 7c0 5.25 7 13 7 13s7-7.75 7-13a7 7 0 0 0-7-7zm0 9.5A2.5 2.5 0 1 1 12 6.5a2.5 2.5 0 0 1 0 5z"/></svg>
            Cedarbrook, OH
          </p>
        </div>
      </div>
    </div>
  </section>

</body>
</html>
```